Need an AWESOME Business Card!!

We need a business card design for a mobile protection company called QuillarDEX. We provide handset protection for mobile devices such as cell phones, smartphones and tablets. We'll get you another device no matter what you do to it- crash, smash or splash, PLUS our protection plan comes with identity theft restoration services, the ability to locate, lock and erase your device and back up your contacts, text, files, pictures and music.
We would like to see the color orange used sparingly in the design. We are looking for something different, creative and fun. Something that will really catch people's attention.
Tagline: Get Protected, Stay Connected
Requirements
Must have
- A place for:
Name
Title
Direct phone #
Toll free #
Twitter
Email
Address
Logo
Website
Nice to have
- QR Code
Technology feel
Should not have
- please do not disassemble our logo icon- the shield shape with power symbol inside should always stay together as seen in our logo. Also- do not recolor our logo. The only variations are all white (power symbol knocked out) or all gray (use the provided swatch ONLY for the gray) Do not alter the colors. For any watermark usage- color should be our gray swatch at 10% opacity.
Thanks!!!

```html
<!DOCTYPE html>
<html lang="en">
<head>
<meta charset="utf-8">
<title>QuillarDEX Business Card</title>
<link rel="stylesheet" href="https://fonts.googleapis.com/css2?family=Open+Sans:wght@400;600;700;800&display=swap">
<style>
  :root {
    --page-bg: #ecebe8;
    --card-bg: #ffffff;
    --orange: #f7941d;
    --orange-faint: #fde3c6;
    --gray: #6d6e71;
    --gray-soft: #d9d9d9;
    --ink: #3a3a3a;
  }
  * { margin: 0; padding: 0; box-sizing: border-box; }
  html, body { width: 1200px; height: 900px; overflow: hidden; }
  body {
    background: var(--page-bg);
    font-family: "Open Sans", Arial, sans-serif;
    color: var(--ink);
    position: relative;
  }
  .card {
    position: absolute;
    left: 320px;
    width: 560px;
    height: 320px;
    background: var(--card-bg);
    border-radius: 10px;
    overflow: hidden;
    box-shadow: 0 4px 14px rgba(0,0,0,0.12);
  }
  .card--front { top: 100px; }
  .card--back { top: 480px; }

  /* Brand */
  .brand {
    position: absolute;
    font-weight: 700;
    color: var(--orange);
    letter-spacing: -0.5px;
    line-height: 1;
    white-space: nowrap;
  }
  .brand__dot {
    display: inline-block;
    width: 0.7em; height: 0.7em;
    border-radius: 50%;
    background: var(--gray);
    margin-right: 8px;
    vertical-align: -0.05em;
  }
  .brand__parent {
    position: absolute;
    font-size: 8px;
    font-weight: 600;
    color: var(--ink);
    white-space: nowrap;
  }

  /* Front */
  .front-brand { right: 40px; top: 28px; font-size: 30px; }
  .front-parent { right: 42px; top: 62px; }
  .rule {
    position: absolute;
    height: 1.5px;
    background: var(--gray);
  }
  .rule--top { left: 210px; right: 0; top: 80px; }
  .rule--name { left: 30px; width: 280px; top: 216px; }
  .watermark {
    position: absolute;
    left: 24px; top: 88px;
    font-size: 62px;
    font-weight: 800;
    color: var(--orange-faint);
    letter-spacing: -1px;
    line-height: 1;
    white-space: nowrap;
  }
  .name {
    position: absolute;
    left: 40px; top: 170px;
    font-size: 32px;
    font-weight: 700;
    color: var(--orange);
    line-height: 1;
    white-space: nowrap;
  }
  .name__title {
    font-size: 13px;
    font-weight: 400;
    color: var(--ink);
    margin-left: 4px;
  }
  .phones {
    position: absolute;
    left: 120px; top: 224px;
    font-size: 17px;
    line-height: 1.4;
    white-space: nowrap;
  }
  .phones__label { color: var(--orange); }
  .phones__row--direct { padding-left: 16px; }
  .contact {
    position: absolute;
    left: 400px; top: 92px;
    font-size: 15px;
    line-height: 1.55;
    white-space: nowrap;
  }
  .contact__row { display: flex; align-items: center; }
  .contact__row--address { padding-left: 22px; }
  .contact__icon {
    width: 13px; height: 13px;
    background: var(--orange);
    border-radius: 2px;
    margin-right: 9px;
  }
  .website {
    position: absolute;
    left: 0; right: 0; top: 284px;
    text-align: center;
    font-size: 17px;
    color: var(--orange);
  }

  /* Back */
  .back-shape {
    position: absolute;
    left: -60px; top: 60px;
    width: 420px; height: 420px;
  }
  .back-brand { right: 34px; bottom: 58px; font-size: 34px; }
  .back-parent { right: 36px; bottom: 42px; font-size: 9px; }
</style>
</head>
<body>

  <section class="card card--front" aria-label="Business card front">
    <div class="watermark" aria-hidden="true">QuillarDEX</div>
    <div class="brand front-brand"><span class="brand__dot"></span>QuillarDEX</div>
    <div class="brand__parent front-parent">a Norvale company</div>
    <div class="rule rule--top"></div>

    <div class="name">John Doe<span class="name__title">Manager</span></div>
    <div class="rule rule--name"></div>
    <div class="phones">
      <div class="phones__row phones__row--direct"><span class="phones__label">p.</span> (312) 408 - 7261</div>
      <div class="phones__row"><span class="phones__label">toll.</span> (866) 204-3187</div>
    </div>

    <div class="contact">
      <div class="contact__row contact__row--address">123 Quillar Dex Ln.</div>
      <div class="contact__row"><span class="contact__icon"></span>QuillarDEX</div>
      <div class="contact__row"><span class="contact__icon"></span>@quillardex</div>
    </div>

    <div class="website">www.quillardex.com</div>
  </section>

  <section class="card card--back" aria-label="Business card back">
    <svg class="back-shape" viewBox="0 0 420 420" aria-hidden="true">
      <circle cx="210" cy="210" r="210" fill="var(--gray-soft)"/>
    </svg>
    <div class="brand back-brand"><span class="brand__dot"></span>QuillarDEX</div>
    <div class="brand__parent back-parent">a Norvale company</div>
  </section>

</body>
</html>
```